Concept design for a tea business Labels

Hello, we are looking for concepts for our label/packaging for a tea business that has been in business now for over a year. We are a beachy, organic, "It's your moment. Enjoy it." type tea business. We have an online website (www.corvalbrewhouse.com.au) and sell at local markets around the Tarrowby Cove area.
We are looking to upgrade our label to look more professional, in a fun/beachy/chilled out style. (unlike the traditional tea labels).
We do loose leaf tea and iced tea consentrated syrups. We have a few different packages (please see website under "sizes and packaging" bottom left). We would like to experiement with various different size and shape of labels for different products, so would like a concept design for a label using our logo (see website front page bottom). There are no colour constraints.
We use the Quillan brand labels of the following sizes:
1. Pure Glass Rectangular Product Labels, Q4825, 100/Pack, 96 x 50.8 mm
2. Pure Glass Round Multi-purpose Labels, Q3907D, 240/Pack, 40 mm diameter
3.Pure Glass Square Product Labels, Q4861, 350/Pack, 35 x 35 mm
4. For bottles we use Grained Ivory Curved Labels, Q4839, 90/Pack, 57.2 x 77 mm
If you have any more questions, please don't hesitate to contact me
Updates
Hi All,
I am considering using a box like below for packing and doing a bit of a white/beachy feel to the packaging. Either using the rectangle or round circle labels. (circle labels from quillan 60mm diameter).

Reason: Hi All - Thank you so much for all your designs. While I have seen some really beautiful designs I am excited about, it seems there was a rush at the end with a number of new designs just submitted. I still haven't seen just one design I love for the label, so I would like the opportunity to work with some of the new designers to see if we can modify to suit the concept.
Would anyone like to try a concept label with a silhouette of one of the following wave/beach/teacup? I'm just exploring a different approach as I know it is difficult tying in the beach with tea - please think - chilled out beach hut with tea/iced tea, sunrise over ocean. I like the soft colour palette - beachy feel to it - ie. Pastels - blues, greens, whites, sandy, pinks, purples, greys - sunrises over ocean, maybe a white rustic wood feel - or any other icon from Tarrowby Cove - like the Norfolk Pine's along the beach - maybe in Silhouette.
Just some more ideas.
Thank you again for all your contributions!
Petra

```html
<!DOCTYPE html>
<html lang="en">
<head>
<meta charset="utf-8">
<title>Tarrowby Tea Company – Organic Green Tea Sencha Label</title>
<link href="https://fonts.googleapis.com/css2?family=Arvo:ital,wght@0,400;1,400&family=Dosis:wght@400;500&display=swap" rel="stylesheet">
<style>
  :root {
    --paper: #ffffff;
    --lime: #d3ff12;
    --leaf-light: #eaff55;
    --leaf-mid: #c6f21a;
    --brand-green: #5f7f00;
    --heading-ink: #262a10;
    --body-ink: #4a5400;
  }
  * { box-sizing: border-box; margin: 0; padding: 0; }
  html, body { width: 892px; height: 1200px; overflow: hidden; background: var(--paper); }
  .label {
    position: relative;
    width: 892px;
    height: 1200px;
    overflow: hidden;
    background: var(--paper);
  }
  .label__arch {
    position: absolute;
    inset: 0;
    background: var(--lime);
    border-radius: 446px 446px 0 0;
  }
  .brand {
    position: absolute;
    top: 58px;
    left: 0;
    width: 892px;
    text-align: center;
    font-family: "Arvo", Georgia, serif;
    color: var(--brand-green);
  }
  .brand__dot {
    display: block;
    width: 192px;
    height: 192px;
    margin: 0 auto 24px 346px;
    border-radius: 50%;
    background: var(--brand-green);
  }
  .brand__name {
    font-size: 40px;
    font-weight: 400;
    line-height: 1.1;
    margin-left: -12px;
  }
  .brand__tagline {
    font-size: 36px;
    font-style: italic;
    line-height: 1.15;
    margin-left: -12px;
  }
  .product {
    position: absolute;
    right: 100px;
    top: 418px;
    text-align: right;
    font-family: "Dosis", "Arial Narrow", sans-serif;
    color: var(--heading-ink);
    font-weight: 500;
  }
  .product__range { font-size: 66px; line-height: 1.05; letter-spacing: -0.5px; }
  .product__name { font-size: 82px; line-height: 1.05; }
  .product__description {
    position: absolute;
    left: 429px;
    top: 612px;
    width: 364px;
    font-family: "Dosis", "Arial Narrow", sans-serif;
    font-weight: 400;
    font-size: 38px;
    line-height: 47px;
    color: var(--body-ink);
    text-align: justify;
    hyphens: manual;
  }
  .illustration {
    position: absolute;
    left: 92px;
    top: 515px;
    width: 310px;
    height: 685px;
  }
</style>
</head>
<body>
  <main class="label">
    <div class="label__arch"></div>

    <header class="brand">
      <span class="brand__dot"></span>
      <p class="brand__name">Tarrowby Tea Company</p>
      <p class="brand__tagline">It’s your moment. Enjoy it.</p>
    </header>

    <h1 class="product">
      <span class="product__range">Organic Green Tea</span><br>
      <span class="product__name">Sencha</span>
    </h1>

    <svg class="illustration" viewBox="0 0 310 685" role="img" aria-label="Line drawing of two tea leaf buds on long stems">
      <defs>
        <linearGradient id="leaf-tone" x1="0" y1="0" x2="1" y2="1">
          <stop offset="0" stop-color="var(--leaf-mid)"/>
          <stop offset="0.5" stop-color="var(--leaf-light)"/>
          <stop offset="1" stop-color="var(--leaf-mid)"/>
        </linearGradient>
      </defs>
      <rect width="310" height="685" rx="40" fill="url(#leaf-tone)"/>
    </svg>

    <p class="product__description">Lorem ipsum dolor sit amet, consecte&shy;tur adipiscing elit. Fusce lacus tellus, gravida et faucibus in, iaculis suscipit nulla. Fusce tellus purus, feugiat eget semper eget, dignis&shy;sim sed lacus. Donec ullamcorper vulpus.</p>
  </main>
</body>
</html>
```